Life Coaching Business Card

Please check out my website at www.lorettavisbeck.com. Ideally I would like to use the same colors that I used on the site to match my business cards i.e: pink, green, teal, white
I want the final design to include a picture of me and also to be appealing and eye catching. For the picture I submitted, you can crop it smaller to just have my face (exclude my chest) showing.
Industry/Entity Type
Business
Contact Information for Business Card
Loretta Visbeck
Transformational Life Coach
web: www.lorettavisbeck.com
email: loretta@lorettavisbeck.com
Phone: 555-318-7042
Look and feel
Each slider illustrates characteristics of the customer's brand and the style your logo design should communicate.

```html
<!DOCTYPE html>
<html lang="en">
<head>
<meta charset="utf-8">
<title>Loretta Visbeck – Business Cards</title>
<link rel="stylesheet" href="https://fonts.googleapis.com/css2?family=Tinos:ital,wght@0,400;1,700&family=Tenor+Sans&family=Open+Sans:wght@600&display=swap">
<style>
  :root {
    --ink: #0d0d1a;
    --page: #ffffff;
    --card-edge: #b9b9b9;
    --teal-light: #e9f6f8;
    --teal: #a3d6dd;
    --teal-band: #8fd4dc;
    --glow: #7fd0e0;
    --plum: #8e3a63;
    --plum-light: #d99abb;
    --pink: #ef7fc8;
    --blue-feather: #1d5fbf;
    --green-feather: #3fa66a;
  }
  * { margin: 0; padding: 0; box-sizing: border-box; }
  html, body {
    width: 1200px; height: 1121px; overflow: hidden;
    background: var(--page);
  }
  .stage {
    position: relative; width: 1200px; height: 1121px;
    display: flex; justify-content: center; align-items: center; gap: 40px;
  }
  .card {
    position: relative; width: 540px; height: 900px;
    border: 2px solid var(--card-edge);
    overflow: hidden;
  }

  /* Front card */
  .card--front {
    background: linear-gradient(160deg, var(--page) 0%, var(--teal-light) 30%, var(--teal) 100%);
  }
  .feather-art {
    position: absolute; left: 50px; top: 50px; width: 260px; height: 300px;
    border-radius: 50% 40% 60% 30%;
    background: radial-gradient(ellipse at 40% 35%, var(--blue-feather) 0%, var(--green-feather) 45%, rgba(63,166,106,0) 70%),
                radial-gradient(ellipse at 70% 85%, var(--pink) 0%, rgba(239,127,200,0) 45%);
    opacity: 0.85;
  }
  .card__name {
    font-family: "Tinos", serif; font-style: italic; font-weight: 700;
    color: var(--ink);
    text-shadow: 0 0 6px var(--glow), 2px 2px 3px rgba(0,0,0,0.25);
    white-space: nowrap;
  }
  .card--front .card__name {
    position: absolute; left: 190px; top: 210px; font-size: 44px;
  }
  .card__title {
    font-family: "Tenor Sans", sans-serif; text-align: center; line-height: 1.15;
    letter-spacing: 0;
    white-space: nowrap;
  }
  .card--front .card__title {
    position: absolute; left: 20px; right: 20px; top: 530px;
    font-size: 39px; color: var(--ink);
    text-shadow: 0 0 6px var(--glow);
  }
  .contact {
    position: absolute; left: 0; right: 0; bottom: 70px;
    font-family: "Tinos", serif; font-size: 28px; color: var(--ink);
    text-align: center; line-height: 1.35;
    white-space: nowrap;
  }

  /* Back card */
  .card--back { background: var(--page); }
  .portrait {
    position: absolute; left: 0; top: 0; width: 100%; height: 560px;
    background: linear-gradient(90deg, #f7c7ea 0%, var(--page) 14%, var(--plum-light) 30%, var(--plum) 60%, #6e2a4d 100%);
  }
  .photo-band {
    position: absolute; left: 80px; right: 0; top: 560px; height: 40px;
    background: linear-gradient(180deg, var(--teal-band), rgba(143,212,220,0));
  }
  .card--back .card__name {
    position: absolute; left: 0; right: 0; top: 600px; text-align: center; font-size: 40px;
  }
  .card--back .card__title {
    position: absolute; left: 20px; right: 20px; top: 690px;
    font-size: 38px; color: var(--page);
    text-shadow: 0 0 2px var(--glow), 0 0 4px var(--glow), 0 0 6px #3fbfb0;
  }
  .card__web {
    position: absolute; left: 0; right: 0; bottom: 50px; text-align: center;
    font-family: "Open Sans", sans-serif; font-weight: 600; font-size: 30px; color: var(--ink);
    white-space: nowrap;
  }
</style>
</head>
<body>
<main class="stage">
  <section class="card card--front">
    <div class="feather-art" role="img" aria-label="Blue, green and pink feathers illustration"></div>
    <h1 class="card__name">Loretta Visbeck</h1>
    <p class="card__title">TRANSFORMATIONAL<br>LIFE COACH</p>
    <p class="contact">
      Web: www.lorettavisbeck.com<br>
      Email: loretta@lorettavisbeck.com<br>
      Phone:&nbsp; 555-318-7042
    </p>
  </section>

  <section class="card card--back">
    <div class="portrait" role="img" aria-label="Portrait photo of the life coach, tinted in plum"></div>
    <div class="photo-band"></div>
    <h2 class="card__name">Loretta Visbeck</h2>
    <p class="card__title">TRANSFORMATIONAL<br>LIFE COACH</p>
    <p class="card__web">www.lorettavisbeck.com</p>
  </section>
</main>
</body>
</html>
```